Business cards and stationary
Law Offices of Delphine R. Okonkwo
Professional
Delphine R. Okonkwo, Esq.
417 N. Cedar Brook Lane
Suite C-320
Plantation, Florida 33991
Delphine@Glenmorelegalcounsel.example
www.Glenmorelegalcounsel.example
The card should match my current website and logo. The back of the card should state: Practice Areas
Estate Planning
Probate and Trust Administration
Tax Law and Structuring
Business Structuring
Please no scales of justice or gavels

```html
<!DOCTYPE html>
<html lang="en">
<head>
<meta charset="utf-8">
<title>Law Offices of Delphine R. Okonkwo — Business Card</title>
<link href="https://fonts.googleapis.com/css2?family=Cinzel:wght@400;600&family=Lato:wght@400;700&display=swap" rel="stylesheet">
<style>
  :root {
    --stage: #e9ebee;
    --card-white: #ffffff;
    --brand-blue: #2f5fd0;
    --brand-blue-deep: #1f45a8;
    --brand-blue-light: #4c7fe6;
    --ink: #16181c;
    --ink-soft: #5d6470;
    --rule: #9aa3b2;
    --silver: #c7ccd4;
    --on-blue: #eef3ff;
  }
  * { box-sizing: border-box; margin: 0; padding: 0; }
  html, body { width: 1200px; height: 1009px; overflow: hidden; }
  body { background: var(--stage); position: relative; font-family: "Lato", sans-serif; }

  .card {
    position: absolute;
    width: 720px; height: 411px;
    border-radius: 22px;
    overflow: hidden;
    box-shadow: 0 10px 28px rgba(20, 30, 50, 0.18);
  }

  /* Back of card */
  .card-back {
    left: 420px; top: 60px;
    background: linear-gradient(135deg, var(--brand-blue-light), var(--brand-blue) 55%, var(--brand-blue-deep));
  }
  .card-back .back-content {
    position: absolute; left: 90px; right: 40px; top: 56px;
    display: flex; flex-direction: column; align-items: center;
  }
  .card-back .mark {
    display: flex; align-items: center; gap: 16px;
  }
  .card-back .mark-square { width: 24px; height: 24px; background: var(--ink); }
  .card-back .mark-name {
    font-family: "Cinzel", serif; font-weight: 600;
    font-size: 60px; line-height: 1; letter-spacing: 4px; color: var(--ink);
  }
  .practice-areas { margin-top: 30px; text-align: center; }
  .practice-title {
    font-family: "Cinzel", serif; font-weight: 600; font-size: 17px;
    letter-spacing: 3px; text-transform: uppercase; color: var(--ink);
    padding-bottom: 10px; margin-bottom: 12px;
    border-bottom: 1px solid rgba(22, 24, 28, 0.45);
  }
  .practice-list { list-style: none; }
  .practice-list li {
    font-family: "Cinzel", serif; font-size: 14px; line-height: 25px;
    letter-spacing: 1px; color: var(--on-blue);
  }
  .card-back .web-vertical {
    position: absolute; left: 62px; top: 205px;
    transform: translate(-50%, -50%) rotate(-90deg);
    font-family: "Cinzel", serif; font-size: 12px; letter-spacing: 3px;
    color: var(--ink); white-space: nowrap;
  }

  /* Front of card */
  .card-front {
    left: 60px; top: 520px;
    background: var(--card-white);
  }
  .card-front .waves { position: absolute; left: 0; top: 0; width: 720px; height: 411px; }

  .firm-block { position: absolute; left: 70px; top: 58px; width: 290px; }
  .firm-mark { display: flex; align-items: center; gap: 12px; }
  .firm-mark .mark-square { width: 16px; height: 16px; background: var(--brand-blue); }
  .firm-mark .mark-name {
    font-family: "Cinzel", serif; font-weight: 600; font-size: 46px;
    letter-spacing: 3px; color: var(--brand-blue);
  }
  .firm-name {
    margin-top: 8px;
    font-family: "Cinzel", serif; font-weight: 600; color: var(--brand-blue);
    text-transform: uppercase; line-height: 1.15;
  }
  .firm-name .lead { display: block; font-size: 15px; letter-spacing: 2px; }
  .firm-name .principal { display: block; font-size: 19px; letter-spacing: 1.5px; }

  .divider {
    position: absolute; left: 372px; top: 112px; width: 1px; height: 150px;
    background: var(--rule);
  }

  .contact-block { position: absolute; left: 390px; top: 108px; width: 310px; }
  .contact-name {
    font-family: "Cinzel", serif; font-size: 14px; color: var(--brand-blue);
    letter-spacing: 0.5px;
  }
  .contact-sub {
    font-family: "Cinzel", serif; font-size: 10px; color: var(--ink-soft);
    letter-spacing: 0.5px; margin-bottom: 6px;
  }
  .contact-list { list-style: none; }
  .contact-list li {
    display: flex; align-items: center; gap: 7px;
    font-size: 10.5px; line-height: 15px; color: var(--ink-soft);
  }
  .contact-list .dot {
    flex: none; width: 9px; height: 9px; border-radius: 50%;
    background: var(--brand-blue);
  }
</style>
</head>
<body>

  <section class="card card-back" aria-label="Back of business card">
    <div class="web-vertical">www.Glenmorelegalcounsel.example</div>
    <div class="back-content">
      <div class="mark">
        <span class="mark-square"></span>
        <span class="mark-name">DRO</span>
      </div>
      <div class="practice-areas">
        <h2 class="practice-title">Practice Areas</h2>
        <ul class="practice-list">
          <li>Estate Planning</li>
          <li>Probate and Trust Administration</li>
          <li>Tax Law and Structuring</li>
          <li>Business Structuring</li>
        </ul>
      </div>
    </div>
  </section>

  <section class="card card-front" aria-label="Front of business card">
    <svg class="waves" viewBox="0 0 720 411" aria-hidden="true">
      <defs>
        <linearGradient id="bandBlue" x1="0" y1="0" x2="1" y2="0">
          <stop offset="0" stop-color="#2a55c4"/>
          <stop offset="0.6" stop-color="#3a6ad8"/>
          <stop offset="1" stop-color="#2f5fd0"/>
        </linearGradient>
      </defs>
      <path d="M0 290 C 160 300, 300 340, 460 350 C 580 356, 660 345, 720 330 L720 411 L0 411 Z" fill="url(#bandBlue)"/>
      <path d="M0 250 C 180 262, 320 320, 470 334 C 590 344, 670 336, 720 322 L720 334 C 660 350, 580 360, 460 352 C 300 340, 160 298, 0 286 Z" fill="#ffffff"/>
      <path d="M0 254 C 180 268, 320 322, 470 336 C 590 346, 670 338, 720 324 L720 332 C 660 348, 580 356, 462 346 C 310 332, 170 286, 0 274 Z" fill="#16181c"/>
      <path d="M0 238 C 180 250, 330 302, 480 318 C 600 330, 670 322, 720 310 L720 314 C 670 328, 600 336, 480 324 C 330 308, 180 258, 0 246 Z" fill="#c7ccd4"/>
    </svg>

    <div class="firm-block">
      <div class="firm-mark">
        <span class="mark-square"></span>
        <span class="mark-name">DRO</span>
      </div>
      <h1 class="firm-name">
        <span class="lead">Law Offices of</span>
        <span class="principal">Delphine R. Okonkwo</span>
      </h1>
    </div>

    <div class="divider"></div>

    <div class="contact-block">
      <p class="contact-name">Delphine R. Okonkwo, Esq.</p>
      <p class="contact-sub">Attorney at Law</p>
      <ul class="contact-list">
        <li><span class="dot"></span>417 N. Cedar Brook Lane</li>
        <li><span class="dot"></span>Suite C-320</li>
        <li><span class="dot"></span>Plantation, Florida 33991</li>
        <li><span class="dot"></span>Tel (555) 014-2290</li>
        <li><span class="dot"></span>Fax (555) 014-2291</li>
        <li><span class="dot"></span>Delphine@Glenmorelegalcounsel.example</li>
        <li><span class="dot"></span>www.Glenmorelegalcounsel.example</li>
      </ul>
    </div>
  </section>

</body>
</html>
```